Tavelin Global Kft. is an online recruitment marketplace connecting the employers and recruiters together. We provide an e-bussiness solution for companies and give busines opportunity for recruiters.
We have a logo design already, which should be used on the business card.
Our colours are grey and magenta, which can be seen in the logo. Black is also welcome.
The style should be dynamic, young but professional. It should be clear, visible, elegant, not too crowded, simple but exciting.
We need the following data on the BC: name, title, address, phone,fax and mobile number, email address, website.
Target Market(s)
Our target market are companies, as this is a B2B business. We also target recruiters, recruitment professionals, headhunters.We would like to be impressive and different.
Industry/Entity Type
Business
Requirements
Must have
- We would like to promote our website, www.tavelglob.hu.
- Please, put this on the back with a quite visible letter size.The style should be dynamic, young but professional. It should be clear, visible, elegant, not too crowded, simple but exciting.
Should not have
- We do not want to see people figures.

```html
<!DOCTYPE html>
<html lang="en">
<head>
<meta charset="utf-8">
<title>Tavelin Global Kft. – Business Card</title>
<link href="https://fonts.googleapis.com/css2?family=Arimo:wght@400;700&display=swap" rel="stylesheet">
<style>
  :root {
    --stage: #000000;
    --paper: #ffffff;
    --magenta: #e5197a;
    --grey: #58585a;
    --grey-text: #5a5a5c;
    --white: #ffffff;
  }
  * { margin: 0; padding: 0; box-sizing: border-box; }
  html, body {
    width: 1200px; height: 900px; overflow: hidden;
    background: var(--stage);
    font-family: "Arimo", Arial, sans-serif;
  }
  .canvas { position: relative; width: 1200px; height: 900px; }

  .card {
    position: absolute; left: 244px; width: 664px; height: 382px;
    border-radius: 22px; overflow: hidden;
  }
  .card--front { top: 40px; background: var(--paper); }
  .card--back { top: 482px; background: var(--grey); }

  .card__band {
    position: absolute; left: 0; right: 0; bottom: 0; height: 30px;
    background: var(--magenta);
  }

  .brand { position: absolute; display: flex; align-items: center; gap: 14px; }
  .brand__mark { display: block; }
  .brand__name { font-weight: 700; white-space: nowrap; }
  .brand--front { left: 344px; top: 48px; }
  .brand--front .brand__name { font-size: 24px; color: var(--grey); }
  .brand--back { left: 0; right: 0; top: 124px; justify-content: center; gap: 18px; }
  .brand--back .brand__name { font-size: 30px; color: var(--white); }

  .holder { position: absolute; left: 38px; top: 120px; }
  .holder__name {
    font-size: 27px; font-weight: 700; color: var(--magenta);
    letter-spacing: 2px;
  }
  .holder__title {
    margin-top: 10px; font-size: 15px; font-weight: 700;
    color: var(--grey-text); letter-spacing: 1.5px;
  }

  .contact { position: absolute; left: 38px; top: 205px; list-style: none; }
  .contact li {
    font-size: 13.5px; font-weight: 700; color: var(--grey-text);
    line-height: 17px;
  }
  .contact__label { color: var(--magenta); margin-right: 3px; }

  .address {
    position: absolute; left: 38px; top: 270px; font-style: normal;
    font-size: 13.5px; font-weight: 700; color: var(--grey-text); line-height: 17px;
  }

  .website {
    position: absolute; left: 0; right: 0; top: 318px; text-align: center;
    font-size: 25px; color: var(--white); letter-spacing: 3px;
  }
  .website strong { font-weight: 700; }
</style>
</head>
<body>
<main class="canvas">

  <section class="card card--front" aria-label="Business card front">
    <div class="brand brand--front">
      <svg class="brand__mark" width="48" height="48" viewBox="0 0 48 48" aria-hidden="true">
        <rect width="48" height="48" fill="var(--magenta)"/>
      </svg>
      <span class="brand__name">Tavelin Global Kft.</span>
    </div>

    <div class="holder">
      <h1 class="holder__name">Mark Halden</h1>
      <p class="holder__title">President</p>
    </div>

    <ul class="contact">
      <li><span class="contact__label">P</span>1300 582 417</li>
      <li><span class="contact__label">F</span>02 9371 5068</li>
      <li><span class="contact__label">E</span>info@tavelglob.hu</li>
    </ul>

    <address class="address">
      Level 2, 41 - 55 Corvin<br>
      St Ferenc Hills 1091
    </address>

    <div class="card__band"></div>
  </section>

  <section class="card card--back" aria-label="Business card back">
    <div class="brand brand--back">
      <svg class="brand__mark" width="70" height="70" viewBox="0 0 70 70" aria-hidden="true">
        <rect width="70" height="70" fill="var(--magenta)"/>
      </svg>
      <span class="brand__name">Tavelin Global Kft.</span>
    </div>
    <p class="website">www.<strong>tavelglob</strong>.hu</p>
  </section>

</main>
</body>
</html>
```